Marketing Postcards

I recently changed real estate companies and want to redo some advertising postcards I've used in the past. I want to replicate the existing cards with updated company info. Please see attached for proofs of old cards as well as the new company logo.

Industry/Entity Type

Real Estate

```html
<!DOCTYPE html>
<html lang="en">
<head>
<meta charset="utf-8">
<title>Marissa Hale – Marketing Postcards</title>
<link href="https://fonts.googleapis.com/css2?family=Libre+Baskerville:wght@400;700&family=Lato:ital,wght@0,400;0,700;1,700&display=swap" rel="stylesheet">
<style>
  :root {
    --plum: #5b2d57;
    --plum-light: #7a4a74;
    --navy: #2c3a8c;
    --navy-light: #4456a8;
    --ink: #1d1d1f;
    --paper: #ffffff;
    --backdrop: #efece8;
    --photo-wall: #e9d79a;
    --photo-floor: #b5834f;
    --portrait: #c9a98a;
    --portrait-dark: #3a5a9a;
  }
  * { box-sizing: border-box; margin: 0; padding: 0; }
  html, body { width: 907px; height: 1200px; overflow: hidden; }
  body { background: var(--backdrop); position: relative; font-family: "Lato", sans-serif; color: var(--ink); }

  .postcard { position: absolute; left: 100px; width: 728px; height: 488px; background: var(--paper); box-shadow: 0 2px 8px rgba(0,0,0,.18); overflow: hidden; }
  .postcard--front { top: 75px; }
  .postcard--back { top: 640px; }

  /* front */
  .front-visual { position: absolute; left: 0; top: 0; width: 465px; height: 488px; }
  .front-visual svg { position: absolute; inset: 0; }
  .brand { position: absolute; left: 20px; top: 27px; display: flex; flex-direction: column; align-items: center; gap: 4px; width: 72px; }
  .brand__mark { width: 44px; height: 44px; border: 2px solid var(--plum); border-radius: 50%; }
  .brand__name { font-family: "Lato", sans-serif; font-weight: 700; font-size: 9px; color: var(--plum); text-align: center; line-height: 1.15; }

  .contact { position: absolute; text-align: right; }
  .postcard--front .contact { right: 155px; top: 38px; }
  .contact__cta { font-family: "Libre Baskerville", serif; font-weight: 700; font-size: 13px; color: var(--ink); }
  .contact__name { font-family: "Libre Baskerville", serif; font-weight: 700; font-size: 25px; color: var(--plum); line-height: 1.3; margin-top: 4px; }
  .contact__phone { font-family: "Libre Baskerville", serif; font-weight: 700; font-size: 22px; color: var(--ink); line-height: 1.3; }
  .contact__line { font-size: 13px; color: var(--plum); line-height: 1.3; }
  .postcard--front .contact__line:first-of-type { margin-top: 4px; }

  .portrait { position: absolute; background: linear-gradient(180deg, var(--portrait) 0%, var(--portrait) 55%, var(--portrait-dark) 100%); }
  .postcard--front .portrait { left: 313px; top: 0; width: 152px; height: 195px; }

  .front-copy { position: absolute; left: 467px; top: 0; width: 261px; height: 488px; background: linear-gradient(180deg, var(--navy) 0%, var(--navy-light) 100%); color: #fff; padding: 36px 18px 0 18px; font-size: 12.4px; font-weight: 700; line-height: 1.3; text-align: justify; }
  .front-copy p + p { margin-top: 17px; }

  /* back */
  .postcard--back .portrait { left: 0; top: 10px; width: 145px; height: 165px; }
  .postcard--back .contact { left: 148px; top: 22px; text-align: left; }
  .postcard--back .contact__name { font-size: 22px; }
  .postcard--back .contact__phone { font-size: 20px; }
  .postcard--back .contact__line:first-of-type { margin-top: 4px; }
  .tagline { font-weight: 700; font-style: italic; font-size: 16px; color: var(--plum); margin-top: 8px; }

  .pledge { position: absolute; left: 0; top: 170px; width: 371px; height: 192px; }
  .pledge svg { position: absolute; inset: 0; }
  .pledge__body { position: absolute; left: 20px; right: 20px; top: 40px; color: #fff; }
  .pledge__address { font-family: "Libre Baskerville", serif; font-weight: 700; font-size: 13.5px; text-transform: uppercase; }
  .pledge__title { font-weight: 700; font-size: 14px; margin-top: 8px; }
  .pledge__text { font-size: 12.4px; line-height: 1.3; text-align: justify; margin-top: 8px; }

  .stamp-box { position: absolute; left: 623px; top: 39px; width: 70px; height: 84px; border: 1px solid #555; }
</style>
</head>
<body>

<section class="postcard postcard--front">
  <div class="front-visual">
    <svg width="465" height="488" viewBox="0 0 465 488" aria-hidden="false">
      <defs>
        <linearGradient id="roomTone" x1="0" y1="0" x2="0" y2="1">
          <stop offset="0" stop-color="var(--photo-wall)"/>
          <stop offset=".6" stop-color="#f1e6c2"/>
          <stop offset="1" stop-color="var(--photo-floor)"/>
        </linearGradient>
      </defs>
      <polygon points="0,190 230,222 465,180 465,196 230,226 0,206" fill="var(--plum)"/>
      <polygon points="0,206 230,226 465,196 465,488 0,488" fill="url(#roomTone)" role="img" aria-label="Photo of a bright living room with sofa, coffee table and wood floor"/>
    </svg>
    <div class="brand">
      <span class="brand__mark"></span>
      <span class="brand__name">Harbor Point Realty</span>
    </div>
    <div class="contact">
      <p class="contact__cta">CALL TODAY!</p>
      <p class="contact__name">MARISSA HALE</p>
      <p class="contact__phone">555-014-2276</p>
      <p class="contact__line">RealtorMarissa@example.com</p>
      <p class="contact__line">www.CoastalCountyHomeFinder.com</p>
    </div>
    <div class="portrait" role="img" aria-label="Portrait photo of the agent"></div>
  </div>
  <div class="front-copy">
    <p>Regardless of whether you plan to sell your home this year, or perhaps down the road, it's never too soon to have a real estate market analysis. Utilize our professional expertise to maximize the return of any future improvements you might be considering.</p>
    <p>As one of the top Real Estate Companies in the Marlow Bay Area, Harborline Realty is uniquely qualified to provide the information you need to ensure your home continues to support your life plans. Harborline Realty's Mall Kiosk will maximize your property's exposure to the local consumers and our low 4.9% marketing is designed to save you money.</p>
    <p>Each assessment is confidential, as custom as the individual property and backed by exceptional results. To learn more, please contact me using the information provided.</p>
  </div>
</section>

<section class="postcard postcard--back">
  <div class="portrait" role="img" aria-label="Portrait photo of the agent"></div>
  <div class="contact">
    <p class="contact__cta">CALL TODAY!</p>
    <p class="contact__name">MARISSA HALE</p>
    <p class="contact__phone">555-014-2276</p>
    <p class="contact__line">RealtorMarissa@example.com</p>
    <p class="contact__line">www.CoastalCountyHomeFinder.com</p>
    <p class="tagline">With you every step of the way!</p>
  </div>
  <div class="pledge">
    <svg width="371" height="192" viewBox="0 0 371 192">
      <defs>
        <linearGradient id="plumTone" x1="0" y1="0" x2="1" y2="1">
          <stop offset="0" stop-color="var(--plum)"/>
          <stop offset="1" stop-color="var(--plum-light)"/>
        </linearGradient>
      </defs>
      <polygon points="0,5 190,25 371,5 371,192 0,192" fill="url(#plumTone)"/>
      <polyline points="0,4 190,24 371,4" fill="none" stroke="#fff" stroke-width="3"/>
      <polyline points="0,0 190,20 371,0" fill="none" stroke="var(--navy)" stroke-width="3"/>
    </svg>
    <div class="pledge__body">
      <p class="pledge__address">2140-B Seaside Blvd., Marlow Bay, NC</p>
      <p class="pledge__title">Complete Confidentiality &amp; No Obligation Pledge</p>
      <p class="pledge__text">Meetings, assessments and correspondence are kept solely between the homeowner and/or the designated representative and do not require a commitment. It is our passion to respond promptly to real estate questions and see creative solutions no matter how great the vision.</p>
    </div>
  </div>
  <div class="stamp-box"></div>
</section>

</body>
</html>
```